Business Card Design

Electronic Security
Alarm Systems
CCTV
Electronic Access Control
Security System Integration

Industry/Entity Type

Business

Contact Information for Business Card

Declan Whitfield
PO Box 862
Carrowbrook Qld 4179
Phone 07 38265014
Mob 0428615937

```html
<!DOCTYPE html>
<html lang="en">
<head>
<meta charset="utf-8">
<title>Kestrel Security Systems – Business Card</title>
<link href="https://fonts.googleapis.com/css2?family=Open+Sans:wght@400;600;700&display=swap" rel="stylesheet">
<style>
  :root {
    --backdrop: #e9e6e1;
    --card: #ffffff;
    --card-shade: #f1f1f1;
    --ink: #2b2b2b;
    --ink-soft: #6d6d6d;
    --rule: #9a9a9a;
    --accent: #f2a51e;
    --accent-deep: #ee8a1c;
    --brand-blue: #35b6e0;
  }
  * { box-sizing: border-box; margin: 0; padding: 0; }
  html, body {
    width: 1200px; height: 1023px; overflow: hidden;
    background: var(--backdrop);
    font-family: "Open Sans", Arial, sans-serif;
    color: var(--ink);
  }
  .business-card {
    position: absolute;
    left: 110px; top: 226px;
    width: 980px; height: 571px;
    background: linear-gradient(135deg, var(--card) 0%, var(--card) 60%, var(--card-shade) 100%);
    border-radius: 4px;
    box-shadow: 0 10px 28px rgba(0,0,0,.18);
  }
  .contact-block {
    position: absolute; left: 70px; top: 70px; width: 470px;
  }
  .person-name {
    font-size: 34px; font-weight: 700; letter-spacing: .5px;
    color: var(--accent); text-transform: uppercase; line-height: 1.1;
  }
  .person-role {
    font-size: 19px; color: var(--ink-soft); margin-top: 6px;
  }
  .divider {
    height: 1px; background: var(--rule); margin: 26px 0 24px; width: 430px;
  }
  .contact-list { list-style: none; font-size: 20px; line-height: 1.55; }
  .contact-list li { display: flex; align-items: center; gap: 12px; }
  .contact-icon {
    width: 20px; height: 20px; border-radius: 3px; background: var(--accent);
    display: inline-flex; align-items: center; justify-content: center; flex: none;
  }
  .contact-address { padding-left: 32px; }
  .services { list-style: none; font-size: 20px; line-height: 1.6; }
  .services li { position: relative; padding-left: 26px; }
  .services li::before {
    content: ""; position: absolute; left: 4px; top: 13px;
    width: 8px; height: 8px; border-radius: 50%; background: var(--accent);
  }
  .brand {
    position: absolute; right: 70px; bottom: 90px;
    display: flex; align-items: center; gap: 18px;
  }
  .brand-mark {
    width: 34px; height: 34px; background: var(--brand-blue); flex: none;
  }
  .brand-name {
    font-size: 44px; font-weight: 600; color: var(--ink); letter-spacing: 1px;
  }
</style>
</head>
<body>
  <article class="business-card">
    <section class="contact-block">
      <h1 class="person-name">Declan Whitfield</h1>
      <p class="person-role">Director</p>
      <div class="divider"></div>
      <ul class="contact-list">
        <li>
          <span class="contact-icon">
            <svg width="12" height="12" viewBox="0 0 12 12" aria-hidden="true"><path d="M3 1l2 2-1 1.5c.6 1.3 1.6 2.3 3 3L8.5 6.5l2 2L9 10.5C5 10 2 7 1.5 3z" fill="#fff"/></svg>
          </span>
          07 38265014
        </li>
        <li>
          <span class="contact-icon">
            <svg width="12" height="12" viewBox="0 0 12 12" aria-hidden="true"><rect x="3" y="1" width="6" height="10" rx="1" fill="#fff"/><rect x="4" y="2.5" width="4" height="5" fill="#f2a51e"/></svg>
          </span>
          0428615937
        </li>
        <li class="contact-address">PO Box 862 Carrowbrook QLD 4179</li>
      </ul>
      <div class="divider"></div>
      <ul class="services">
        <li>Electronic Security</li>
        <li>Alarm Systems</li>
        <li>CCTV</li>
        <li>Electronic Access Control</li>
        <li>Security System Integration</li>
      </ul>
    </section>
    <div class="brand">
      <span class="brand-mark"></span>
      <span class="brand-name">Kestrel</span>
    </div>
  </article>
</body>
</html>
```